CuraNex System Web Page Design

This project is to design 6 pages of a web based medical system for clinics, hospitals, drugs suppliers, general items suppliers, insurance company, laboratories and patients (basically all parties which could be involved in).We want the designs of the browser, button, icon and layout are based on Vex, which is user friendly, looks professional, simple and neat but with powerful functions. We have uploaded few pictures of another system, please do not copy its design because this is not what we are looking for, the pictures are for you to know the elements should be included in our pages. CuraNex web-base system, design 6 pages1. Login PageShould include the following elements-company id with input field-login id with input field-password with input field2. Main Page (Navigation page)Should include the following elements-Appointment-Consultation-Patient-Drugs inventory -General supplies inventory -Laboratory-Suppliers-Insurance-Reports 3. Appointment PageShould include all the the elements in the respective pictures plus the followings-Daily View, Weekly View, Monthly View buttons4. Consultation PageShould include all the the elements in the respective picture5. Patient Page5.1 General information Should include all the the elements in the respective picture5.2 medical history/lab reportsShould include all the the elements in the respective picture plus the followings-Notify patient button-Share report button.
Updated on 28 Nov:
Please stop using Ward Keystone in your designs which is not the name of our system. We have just rename our system to CuraNex, please take note.
We need the system to look professional not playful, do not use too many colors and playful icons.
professional users

```html
<!DOCTYPE html>
<html lang="en">
<head>
<meta charset="utf-8">
<title>CuraNex — Sign In</title>
<link href="https://fonts.googleapis.com/css2?family=Open+Sans:wght@300;400;700&display=swap" rel="stylesheet">
<style>
  :root {
    --page-bg: #ffffff;
    --panel-top: #0b3a8c;
    --panel-mid: #0d6fa8;
    --panel-bottom: #15a7b2;
    --hero-light: #6f9fc0;
    --hero-mid: #3f78a8;
    --hero-deep: #24578f;
    --accent: #f98c0a;
    --text-light: #ffffff;
    --text-soft: rgba(255,255,255,0.78);
    --field-line: rgba(255,255,255,0.6);
    --placeholder: rgba(255,255,255,0.55);
  }
  * { box-sizing: border-box; margin: 0; padding: 0; }
  html, body { width: 1200px; height: 1200px; overflow: hidden; background: var(--page-bg); font-family: "Open Sans", sans-serif; }
  .login-band { position: absolute; left: 0; top: 226px; width: 1200px; height: 750px; display: flex; }
  .login-panel { position: relative; width: 582px; height: 100%; background: linear-gradient(180deg, var(--panel-top) 0%, var(--panel-mid) 50%, var(--panel-bottom) 100%); color: var(--text-light); }
  .hero-visual { position: relative; flex: 1; height: 100%; background:
      radial-gradient(circle at 30% 35%, var(--hero-deep) 0%, transparent 45%),
      radial-gradient(circle at 80% 25%, var(--hero-light) 0%, transparent 50%),
      linear-gradient(160deg, var(--hero-light) 0%, var(--hero-mid) 55%, var(--hero-deep) 100%); }
  .brand { position: absolute; left: 0; width: 100%; top: 160px; text-align: center; font-weight: 700; font-size: 46px; letter-spacing: 0.5px; }
  .field { position: absolute; left: 107px; width: 368px; height: 40px; border-bottom: 1px solid var(--field-line); display: flex; align-items: center; gap: 14px; padding-left: 4px; }
  .field svg { width: 20px; height: 20px; flex: none; }
  .field input { background: none; border: none; outline: none; color: var(--text-light); font-family: inherit; font-size: 12px; width: 100%; }
  .field input::placeholder { color: var(--placeholder); }
  .field--company { top: 276px; }
  .field--user { top: 330px; }
  .field--password { top: 382px; }
  .sign-in { position: absolute; left: 197px; top: 473px; width: 186px; height: 54px; border: none; border-radius: 27px; background: var(--accent); color: var(--text-light); font-family: inherit; font-weight: 700; font-size: 18px; letter-spacing: 1px; }
  .forgot { position: absolute; left: 0; width: 100%; top: 545px; text-align: center; font-size: 12.5px; color: var(--text-soft); }
  .signup-note { position: absolute; left: 0; width: 100%; top: 640px; text-align: center; font-size: 13.5px; color: var(--text-soft); }
  .signup-note a { color: var(--text-soft); text-decoration: underline; }
  .tagline { position: absolute; left: 0; width: 100%; top: 278px; text-align: center; color: var(--text-light); }
  .tagline__lead { font-weight: 300; font-size: 37px; line-height: 46px; }
  .tagline__parties { font-weight: 700; font-size: 34px; line-height: 41.5px; }
</style>
</head>
<body>
  <main class="login-band">
    <section class="login-panel">
      <div class="brand">CuraNex</div>

      <label class="field field--company">
        <svg viewBox="0 0 20 20" fill="none" stroke="#ffffff" stroke-width="1" opacity="0.8"><rect x="1" y="4" width="18" height="12"/><rect x="3.5" y="6.5" width="5" height="6"/><line x1="10.5" y1="7.5" x2="17" y2="7.5"/><line x1="10.5" y1="10" x2="17" y2="10"/><line x1="10.5" y1="12.5" x2="15" y2="12.5"/></svg>
        <input type="text" placeholder="Company id">
      </label>

      <label class="field field--user">
        <svg viewBox="0 0 20 20" fill="none" stroke="#ffffff" stroke-width="1.2" opacity="0.8"><circle cx="10" cy="6" r="3.5"/><path d="M3 18c0-4 3-6.5 7-6.5s7 2.5 7 6.5"/></svg>
        <input type="text" placeholder="Username">
      </label>

      <label class="field field--password">
        <svg viewBox="0 0 20 20" fill="none" stroke="#ffffff" stroke-width="1.2" opacity="0.8"><path d="M5 9V6.5a5 5 0 0 1 10 0V9"/><rect x="2.5" y="9" width="15" height="9"/><circle cx="10" cy="12.5" r="1.2"/><line x1="10" y1="13.5" x2="10" y2="15.5"/></svg>
        <input type="password" placeholder="*******">
      </label>

      <button class="sign-in" type="button">SIGN IN</button>
      <p class="forgot">Forgot Password?</p>
      <p class="signup-note">Don’t have an account ? <a href="#">Sign up</a></p>
    </section>

    <section class="hero-visual" role="img" aria-label="Blue medical illustration of a human anatomy figure with DNA strands and soft bokeh lights">
      <div class="tagline">
        <p class="tagline__lead">Medical system for</p>
        <p class="tagline__parties">Clinics, Hospitals, Drugs<br>Suppliers, Insurance company,<br>Laboratories &amp; Patients</p>
      </div>
    </section>
  </main>
</body>
</html>
```